WEBSITE DESIGN - www.brondellix.com

We need a professional and modern looking website for our business. The current website was only made tentatively and can be viewed (we expect a website MUCH better than this). It needs to be simple and non-cluttered yet look modern and sophisticated. It needs to be very easy to navigate as our tarket market is people over the age of 45. Our logo is attached below and this should be incorporated plus the colours/theme should match this. We don't mind purchasing images online if your design includes these and we like it.

Any other specific questions please enquire as we want to hear them.

Target Market(s)

over 45 age english speaking westerners

Industry/Entity Type

Business

Number of Pages Required

1 page

Requirements
Must have
• -our logo (attached).
• -page tabs as those described (tabs.. but not necessarily each of these pages completed as well although this would be nice).
• -social media logos
• Pages should include: homepage, services, pricing, about us, contact us. There should also be a payments page designed which would link with the other pages but there would be no tab for this.

```html
<!DOCTYPE html>
<html lang="en">
<head>
<meta charset="utf-8">
<title>Brondellix – Web Designing &amp; Support</title>
<link rel="stylesheet" href="https://fonts.googleapis.com/css2?family=Open+Sans:wght@400;600;700&family=Raleway:wght@400;600;700&display=swap">
<style>
:root{
  --gold:#f6b92c;
  --gold-dark:#e3a314;
  --brown:#8a5a10;
  --ink:#2b2b2b;
  --charcoal:#1f1f1f;
  --text:#555;
  --muted:#888;
  --paper:#ffffff;
  --mist:#efefef;
}
*{margin:0;padding:0;box-sizing:border-box}
html,body{width:1200px;height:3666px;overflow:hidden}
body{position:relative;font-family:"Open Sans",Arial,sans-serif;color:var(--text);background:var(--paper)}
.abs{position:absolute}
h2{font-family:"Raleway","Open Sans",sans-serif;font-weight:400}

/* header / hero */
.hero{left:0;top:0;width:1200px;height:582px;background:linear-gradient(135deg,#6d7680 0%,#b9bfc4 35%,#d9d4c8 65%,#8a8276 100%)}
.hero-shade{left:0;top:0;width:1200px;height:582px;background:rgba(0,0,0,.18)}
.brand{left:171px;top:0;width:196px;height:150px;background:var(--paper);display:flex;align-items:center;justify-content:center;gap:10px}
.brand-dot{width:22px;height:22px;border-radius:50%;background:var(--gold)}
.brand-name{font-family:"Open Sans",sans-serif;font-weight:700;font-size:26px;color:var(--ink)}
.nav{top:30px;left:528px;display:flex;gap:0}
.nav a{display:block;padding:0 17px;height:50px;line-height:24px;font-size:15px;font-weight:600;color:#fff;text-decoration:none;font-family:"Raleway",sans-serif}
.nav a.active{color:var(--gold);border-bottom:3px solid var(--gold)}
.hero-title{left:0;top:262px;width:1200px;text-align:center;color:#fff;font-family:"Raleway",sans-serif;font-weight:700;font-size:50px;letter-spacing:1px}
.hero-sub{left:0;top:324px;width:1200px;text-align:center;color:#fff;font-family:"Raleway",sans-serif;font-weight:700;font-size:28px}
.hero-arrow{top:426px;width:34px;height:34px;background:rgba(255,255,255,.35)}
.dots{left:560px;top:550px;display:flex;gap:8px}
.dots span{width:13px;height:13px;border-radius:50%;background:rgba(255,255,255,.6)}
.dots span.on{background:#fff}

/* features band */
.features{left:0;top:582px;width:1200px;height:230px}
.feature{top:640px;width:230px;text-align:center;color:#fff}
.feature svg{display:block;margin:0 auto 14px}
.feature h3{font-family:"Raleway",sans-serif;font-size:15px;font-weight:700;letter-spacing:.5px}
.feature p{font-size:10.5px;line-height:15px;margin-top:6px;color:#fff6dd}

/* intro */
.intro-title{left:0;top:916px;width:1200px;text-align:center;font-size:30px;line-height:38px;color:var(--ink)}
.intro-copy{left:170px;top:1002px;width:860px;text-align:center;font-size:12.5px;line-height:22px;color:var(--text)}

/* why */
.why{left:0;top:1154px;width:1200px;height:503px;background:linear-gradient(135deg,#4b4640,#7c7467 50%,#3d3833)}
.why-title{left:0;top:1186px;width:1200px;text-align:center;font-size:22px;color:#fff;font-weight:600}
.tile{width:217px;height:176px;padding:22px 18px;text-align:center;color:#fff}
.tile h4{font-family:"Raleway",sans-serif;font-size:14px;font-weight:700;margin-bottom:8px}
.tile p{font-size:10px;line-height:14px}
.tile.dark{background:#2a2a2a}
.tile.yellow{background:var(--gold)}
.tile.photo-a{background:linear-gradient(135deg,#c8c8c8,#6a6a6a)}
.tile.photo-b{background:linear-gradient(135deg,#1f5a8c,#7bb6e0)}
.tile.photo-c{background:linear-gradient(135deg,#2b3e6e,#6a8bc4)}
.tile.photo-d{background:linear-gradient(135deg,#d7d7d7,#9b9b9b)}

/* stats */
.stats{left:0;top:1657px;width:1200px;height:220px;background:linear-gradient(180deg,#c7861a,var(--brown) 60%,#6e470c)}
.stat{top:1710px;width:140px;text-align:center;color:#fff}
.stat svg{display:block;margin:0 auto 10px;opacity:.75}
.stat .label{font-family:"Raleway",sans-serif;font-size:14px;font-weight:600}
.stat .num{font-size:27px;font-weight:700;margin-top:6px}

/* pricing */
.pricing-title{left:0;top:1910px;width:1200px;text-align:center;font-size:27px;color:var(--gold-dark)}
.plan{background:#fff;text-align:center;border:1px solid #e2e2e2}
.plan-head{height:52px;line-height:52px;color:#fff;font-family:"Raleway",sans-serif;font-weight:700;font-size:17px}
.plan .price{color:var(--gold-dark);font-size:14px;line-height:21px;font-weight:600;margin-top:18px}
.plan .fine{font-size:9.5px;line-height:13px;color:var(--muted);padding:12px 26px 8px}
.plan .feat{font-size:11.5px;line-height:25px;color:var(--text)}
.btn{display:inline-block;background:var(--gold);color:#fff;font-weight:700;font-size:12.5px;border-radius:20px;padding:9px 22px;margin-top:16px}

/* testimonials */
.testi{left:0;top:2420px;width:1200px;height:403px;background:var(--mist)}
.testi-title{left:0;top:2480px;width:1200px;text-align:center;font-size:25px;color:var(--ink)}
.quote{top:2542px;width:398px;height:148px;background:#fff;padding:28px 30px;text-align:center;font-size:12px;line-height:21px;color:var(--text)}
.person{top:2702px;display:flex;align-items:center;gap:14px}
.avatar{width:56px;height:56px;border-radius:50%;background:linear-gradient(135deg,#e6c3a8,#b98e6e)}
.person .name{font-size:13px;color:var(--ink)}
.person .loc{font-size:10.5px;color:var(--muted)}

/* map */
.map{left:0;top:2823px;width:1200px;height:384px;background:linear-gradient(135deg,#e9e5da,#f3efe4 45%,#a9cde8 70%,#eae6dc)}

/* contact */
.contact{left:0;top:3207px;width:1200px;height:405px;background:linear-gradient(180deg,#2c2c2c,#1b1b1b)}
.contact-title{left:0;top:3248px;width:1200px;text-align:center;font-size:28px;color:#fff}
.field{left:191px;width:342px;height:31px;border:1px solid #bdbdbd;background:transparent;color:#ddd;font-size:11.5px;padding:7px 10px}
.send{left:191px;top:3539px;width:92px;height:35px;background:var(--gold);color:#fff;font-weight:700;font-size:13px;text-align:center;line-height:35px}
.address{left:606px;top:3316px;color:#e3e3e3;font-size:12px;line-height:24.5px}
.social{left:606px;top:3455px;display:flex;gap:10px}
.social span{width:22px;height:22px;border-radius:50%;background:var(--gold)}
.reach{left:831px;top:3316px;color:#e3e3e3;font-size:12px;line-height:24.5px}
.footer{left:0;top:3612px;width:1200px;height:54px;background:#111;color:#aaa;font-size:11px;text-align:center;line-height:54px}
</style>
</head>
<body>

<!-- Header & hero -->
<div class="abs hero" role="img" aria-label="Desk scene with a laptop showing a web design layout, a lamp and office items"></div>
<div class="abs hero-shade"></div>
<div class="abs brand"><span class="brand-dot"></span><span class="brand-name">Brondellix</span></div>
<nav class="abs nav">
  <a class="active">HOME</a><a>SERVICES</a><a>PRICING</a><a>ABOUT US</a><a>CONTACT US</a>
</nav>
<div class="abs hero-title">WEB DESIGNING &amp; SUPPORT</div>
<div class="abs hero-sub">FAMES AC TURPIS EGESTAS CRAS</div>
<div class="abs hero-arrow" style="left:158px"><svg width="34" height="34"><path d="M20 10 13 17 20 24" fill="none" stroke="#fff" stroke-width="2"/></svg></div>
<div class="abs hero-arrow" style="left:1002px"><svg width="34" height="34"><path d="M14 10 21 17 14 24" fill="none" stroke="#fff" stroke-width="2"/></svg></div>
<div class="abs dots"><span class="on"></span><span></span><span></span></div>

<!-- Features band -->
<svg class="abs features" width="1200" height="230" viewBox="0 0 1200 230">
  <polygon points="0,0 1200,0 1200,220 600,176 0,220" fill="var(--gold)"/>
</svg>
<div class="abs feature" style="left:125px">
  <svg width="56" height="56" viewBox="0 0 56 56" fill="none" stroke="#fff" stroke-width="2.5"><rect x="6" y="6" width="44" height="44" rx="4"/><path d="M18 40 34 24M34 16a6 6 0 1 0 6 6"/></svg>
  <h3>TECH SUPPORT</h3><p>Fast friendly help for every device<br>you own at home or office</p>
</div>
<div class="abs feature" style="left:349px">
  <svg width="56" height="56" viewBox="0 0 56 56" fill="none" stroke="#fff" stroke-width="2.5"><path d="M16 36a10 10 0 0 1 2-20 13 13 0 0 1 24 4 8 8 0 0 1-2 16"/><path d="M28 26v20M21 39l7 7 7-7"/></svg>
  <h3>DOWNLOAD</h3><p>Safe trusted software ready for<br>your computer in a few clicks</p>
</div>
<div class="abs feature" style="left:569px">
  <svg width="56" height="56" viewBox="0 0 56 56" fill="none" stroke="#fff" stroke-width="2.5"><rect x="6" y="10" width="44" height="30" rx="2"/><path d="M22 48h12M28 40v8"/></svg>
  <h3>WEB DESIGN</h3><p>Clean modern websites built to<br>suit your business and budget</p>
</div>
<div class="abs feature" style="left:794px">
  <svg width="56" height="56" viewBox="0 0 56 56" fill="none" stroke="#fff" stroke-width="2.5"><path d="M44 12c-12 0-20 8-24 18l6 6c10-4 18-12 18-24zM20 30l-8 2 4-8h8M26 36l-2 8 8-4v-8"/><circle cx="36" cy="20" r="3"/></svg>
  <h3>UNDERSTAND THE URGENCY</h3><p>Quick response when things go<br>wrong so you stay online</p>
</div>

<!-- Intro -->
<h2 class="abs intro-title">Our Customer Our Priority<br>Lets Say Hi..</h2>
<p class="abs intro-copy">Brondellix was established to provide consumers with access to the sophisticated, enterprise-level IT services, support and the benefits and cost savings available to larger organisations. We provide proactive monitoring and management of customers entire IT needs. Brondellix is a growing organisation dedicated to making your PC tech support easy and accessible.</p>

<!-- Why we are the best -->
<div class="abs why" role="img" aria-label="Blurred office desk with computer and coffee cup"></div>
<h2 class="abs why-title">Why We Are The Best</h2>
<div class="abs tile photo-a" style="left:166px;top:1234px" role="img" aria-label="Technician repairing a laptop"></div>
<div class="abs tile dark" style="left:383px;top:1234px"><h4>SETUP &amp; INSTALL</h4><p>Confused and frustrated with device setup &amp; installation? Leave it to the experts, which means all you're to do is relax.</p></div>
<div class="abs tile photo-c" style="left:600px;top:1234px" role="img" aria-label="Search optimisation concept graphic"></div>
<div class="abs tile dark" style="left:817px;top:1234px"><h4>WEB DESIGNING</h4><p>We develop the website, we analyse, research and study your needs and approach the not only create website - we create a Brand.</p></div>
<div class="abs tile yellow" style="left:166px;top:1410px"><h4>DIAGNOSIS<br>&amp; REPAIR</h4><p>We find the fault fast, explain it in plain words and repair it at a fair price.</p></div>
<div class="abs tile photo-b" style="left:383px;top:1410px" role="img" aria-label="Abstract blue technology light"></div>
<div class="abs tile yellow" style="left:600px;top:1410px"><h4>OPTIMIZATION</h4><p>You won't believe it's the same old computer. Your system will work like it did on the day you bought it by installing updates, anywhere devices and tools for your home devices.</p></div>
<div class="abs tile photo-d" style="left:817px;top:1410px" role="img" aria-label="Laptop with design mockups on a desk"></div>

<!-- Stats -->
<div class="abs stats"></div>
<div class="abs stat" style="left:175px"><svg width="34" height="28" viewBox="0 0 34 28" fill="none" stroke="#fff" stroke-width="2"><rect x="5" y="3" width="24" height="16"/><path d="M1 24h32"/></svg><div class="label">LAPTOPS</div><div class="num">986</div></div>
<div class="abs stat" style="left:304px"><svg width="34" height="28" viewBox="0 0 34 28" fill="none" stroke="#fff" stroke-width="2"><rect x="3" y="15" width="28" height="10"/><path d="M10 15 8 3M24 15l2-12"/></svg><div class="label">ROUTERS</div><div class="num">256</div></div>
<div class="abs stat" style="left:455px"><svg width="34" height="28" viewBox="0 0 34 28" fill="none" stroke="#fff" stroke-width="2"><rect x="11" y="1" width="12" height="26" rx="2"/></svg><div class="label">SMART PHONES</div><div class="num">867</div></div>
<div class="abs stat" style="left:617px"><svg width="34" height="28" viewBox="0 0 34 28" fill="none" stroke="#fff" stroke-width="2"><rect x="3" y="2" width="28" height="18"/><path d="M11 26h12M17 20v6"/></svg><div class="label">DESKTOPS</div><div class="num">1904</div></div>
<div class="abs stat" style="left:751px"><svg width="34" height="28" viewBox="0 0 34 28" fill="none" stroke="#fff" stroke-width="2"><rect x="7" y="2" width="20" height="24" rx="2"/></svg><div class="label">TABLETS</div><div class="num">511</div></div>
<div class="abs stat" style="left:886px"><svg width="34" height="28" viewBox="0 0 34 28" fill="none" stroke="#fff" stroke-width="2"><rect x="4" y="10" width="26" height="16"/><path d="M24 10V2"/></svg><div class="label">SOFTWARE</div><div class="num">2456</div></div>

<!-- Pricing -->
<h2 class="abs pricing-title">Our Pricing</h2>
<div class="abs plan" style="left:205px;top:2004px;width:250px;height:362px">
  <div class="plan-head" style="background:#4a4a4a">QUICK FIX</div>
  <div class="price">NZD 95<br>USD 60*<br>GBP 40*</div>
  <p class="fine">The price advertised might not be the same price charged to the credit card account due to exchange rate fluctuations This means that because we are based in New Zealand</p>
  <div class="feat">1 Month Tech Support<br>For 1 Computer<br>24X7 Availability</div>
  <span class="btn">ORDER NOW</span>
</div>
<div class="abs plan" style="left:455px;top:1975px;width:273px;height:402px;box-shadow:0 4px 18px rgba(0,0,0,.18);z-index:2">
  <div class="plan-head" style="background:var(--gold);height:60px;line-height:60px">STARTER</div>
  <div class="price">NZD 140<br>USD 90*<br>GBP 60</div>
  <p class="fine">The price advertised might not be the same price charged to the credit card account due to exchange rate fluctuations This means that because we are based in New Zealand</p>
  <div class="feat">6 Month Tech Support<br>6 Month support for the same issue<br>24X7 Availability</div>
  <span class="btn">ORDER NOW</span>
</div>
<div class="abs plan" style="left:728px;top:2004px;width:250px;height:362px">
  <div class="plan-head" style="background:#111">ADVANCE</div>
  <div class="price">NZD 250<br>USD 160*<br>GBP 105*</div>
  <p class="fine">The price advertised might not be the same price charged to the credit card account due to exchange rate fluctuations This means that because we are based in New Zealand</p>
  <div class="feat">1 Year Tech Support<br>Upto 3 Computers &amp; Printers<br>Connected Devices with Router</div>
  <span class="btn">ORDER NOW</span>
</div>

<!-- Testimonials -->
<div class="abs testi"></div>
<h2 class="abs testi-title">What Our Client Says</h2>
<div class="abs quote" style="left:196px">Thank for such a support. Quality Support. I'm extremely impressed. It has been on of the best expirence. So Pleased with u Brondellix. You r best.</div>
<div class="abs quote" style="left:611px">Thanks Brondellix. That was a huge help and exactly what I was looking for. I appreciate the help, you probably saved me 5 horus of frustration right there</div>
<div class="abs person" style="left:309px"><div class="avatar" role="img" aria-label="Client portrait"></div><div><div class="name">Nora Welling</div><div class="loc">City, Location</div></div></div>
<div class="abs person" style="left:714px"><div class="avatar" role="img" aria-label="Client portrait"></div><div><div class="name">Dana Prewitt</div><div class="loc">City, Location</div></div></div>

<!-- Map -->
<div class="abs map" role="img" aria-label="Street map of the city centre with office location pin"></div>

<!-- Contact -->
<div class="abs contact" role="img" aria-label="Dark desk with camera and accessories seen from above"></div>
<h2 class="abs contact-title">Contact Us</h2>
<div class="abs field" style="top:3317px">Name</div>
<div class="abs field" style="top:3358px">Email address</div>
<div class="abs field" style="top:3400px">Phone</div>
<div class="abs field" style="top:3442px;height:85px">Message</div>
<div class="abs send">SEND</div>
<div class="abs address">Keystone Tech Services Limited<br>Marlow Gardens Tower 1<br>4B/118 Marlow Street<br>Auckland Central<br>Auckland-1010,New Zealand</div>
<div class="abs social"><span></span><span></span><span></span><span></span><span></span></div>
<div class="abs reach">USA - +1 555 010 2841<br>UK - +44 20 7946 0312<br>Australia - +61 2 5550 1184<br>For Query - info@brondellix.com<br>For Billing - bills@brondellix.com<br>For Support - support@brondellix.com</div>
<div class="abs footer">© 2016 Company Name  All right reserved</div>

</body>
</html>
```